Young Accounting firm needing a captivating business card

We need a business card design that forces the person to look at the card because its either gold foil, plastic, or lettering pop up etc. We already have a logo with a specific gold color and we need to make it pop. We are an accounting firm. I need the words" accounting, payroll, licenses, audits, taxes" somewhere on the business card so as to describe what we do- preferably on the side where the logo is at.

Industry/Entity Type

Accounting

Contact Information for Business Card

Address 48276 9th Ave S Ste 305, Federal Way, WA 98117
Business Phone (360)418-2096
Fax (360)418-2157
Office Cell Phone (360)586-7319

Font styles to use
Serif

Colors
85abd2

Requirements
Must have
• It should state
• "Accounting" "Taxes" "Audits" "Licenses" "Payroll"
Nice to have
• Matte with gold foil, different textures, With Either a textured ivory background or gray blue slate background
Should not have
• colorful colors

```html
<!DOCTYPE html>
<html lang="en">
<head>
<meta charset="utf-8">
<title>Kestrel Ledger – Business Card</title>
<link href="https://fonts.googleapis.com/css2?family=Poppins:wght@400;500;600&display=swap" rel="stylesheet">
<style>
  :root {
    --backdrop: #3a3b3d;
    --card: #1c1c1d;
    --gold: #c9963f;
    --gold-light: #e3b766;
    --text-soft: #cfcfcf;
    --divider: #55555a;
  }
  * { margin: 0; padding: 0; box-sizing: border-box; }
  html, body { width: 1200px; height: 885px; overflow: hidden; }
  body {
    background: var(--backdrop);
    font-family: "Poppins", sans-serif;
    position: relative;
  }
  .card {
    position: absolute;
    width: 600px;
    height: 343px;
    background: var(--card);
    border-radius: 4px;
    box-shadow: 0 14px 30px rgba(0,0,0,.45);
    overflow: hidden;
  }
  .card--front { left: 70px; top: 70px; }
  .card--back { left: 530px; top: 470px; }

  .brand {
    display: flex;
    align-items: center;
    gap: 14px;
    color: var(--gold);
    font-weight: 500;
    white-space: nowrap;
  }
  .brand__mark { background: var(--gold); flex: none; }

  .card--front .brand {
    position: absolute;
    left: 60px; top: 50%;
    transform: translateY(-50%);
    font-size: 52px;
    letter-spacing: -0.5px;
  }
  .card--front .brand__mark { width: 120px; height: 120px; }

  .back__identity {
    position: absolute;
    left: 0; top: 0;
    width: 290px; height: 280px;
    display: flex; align-items: center; justify-content: center;
  }
  .back__identity .brand {
    flex-direction: column;
    gap: 12px;
    font-size: 32px;
  }
  .back__identity .brand__mark { width: 56px; height: 56px; }

  .back__divider {
    position: absolute;
    left: 296px; top: 28px;
    width: 1px; height: 230px;
    background: var(--divider);
  }

  .contact {
    position: absolute;
    left: 318px; top: 34px;
    color: var(--text-soft);
    font-size: 12px;
    line-height: 1.5;
  }
  .contact__name { color: var(--gold-light); font-size: 18px; font-weight: 600; line-height: 1.2; }
  .contact__role { color: #fff; font-size: 12px; font-weight: 500; margin-bottom: 10px; }
  .contact__address { margin-bottom: 10px; }
  .contact__list { list-style: none; }
  .contact__list li { display: flex; align-items: center; gap: 8px; }
  .contact__list svg { width: 11px; height: 11px; fill: var(--gold-light); flex: none; }

  .services-band {
    position: absolute;
    left: 0; right: 0; bottom: 28px;
    height: 32px;
    background: var(--gold);
    color: #fff;
    font-size: 13px;
    font-weight: 500;
    display: flex; align-items: center;
    padding-left: 130px;
    letter-spacing: .2px;
  }
  .services-band__mark {
    position: absolute;
    right: 18px; top: -12px;
    width: 30px; height: 30px;
    background: var(--gold-light);
    border: 3px solid var(--card);
  }
</style>
</head>
<body>
  <section class="card card--front" aria-label="Card front">
    <div class="brand">
      <span class="brand__mark"></span>
      <span class="brand__name">Kestrel Ledger</span>
    </div>
  </section>

  <section class="card card--back" aria-label="Card back">
    <div class="back__identity">
      <div class="brand">
        <span class="brand__mark"></span>
        <span class="brand__name">Kestrel Ledger</span>
      </div>
    </div>
    <div class="back__divider"></div>

    <div class="contact">
      <p class="contact__name">Daniel Mercer</p>
      <p class="contact__role">Founder &amp; CEO</p>
      <p class="contact__address">48276 9th Ave S Ste 305,<br>Federal Way, WA 98117</p>
      <ul class="contact__list">
        <li><svg viewBox="0 0 12 12"><path d="M2 1h3l1 3-2 1a7 7 0 0 0 3 3l1-2 3 1v3c0 .6-.4 1-1 1A10 10 0 0 1 1 2c0-.6.4-1 1-1z"/></svg>(360)418-2096</li>
        <li><svg viewBox="0 0 12 12"><path d="M3 0h6a1 1 0 0 1 1 1v10a1 1 0 0 1-1 1H3a1 1 0 0 1-1-1V1a1 1 0 0 1 1-1zm0 2v7h6V2z"/></svg>(360)586-7319</li>
        <li><svg viewBox="0 0 12 12"><path d="M3 0h5v3H3zM1 4h10v5H9v3H3V9H1zm3 5v2h4V9z"/></svg>(360)418-2157</li>
        <li><svg viewBox="0 0 12 12"><path d="M0 2h12v8H0zm1 1v.3l5 3.4 5-3.4V3z"/></svg>info@kestrelledger.com</li>
        <li><svg viewBox="0 0 12 12"><circle cx="6" cy="6" r="5.5"/></svg>www.kestrelledger.com</li>
      </ul>
    </div>

    <div class="services-band">
      Accounting • Taxes • Audits • Licenses • Payroll
      <span class="services-band__mark"></span>
    </div>
  </section>
</body>
</html>
```